Poster Design Project

Hi Guys

I am needing an A3 poster design; I basically need a wall chart/ poster that teachers our bakeries how to make the perfect Scone.

I would like our "Florwick" branding to be prominent and these will be hung on bakery production areas for people to utilise when making scones.

Whilst the information needs to be clear I would also like it to be pleasing to the eye and have a "bakery' feel.

Many thanks in advance.

Dean

Target Market(s)

Bakery Production area.

Industry/Entity Type

Bakery

```html
<!DOCTYPE html>
<html lang="en">
<head>
<meta charset="utf-8">
<title>Scone Perfection – Florwick Wall Chart</title>
<link href="https://fonts.googleapis.com/css2?family=Open+Sans:wght@400;600&display=swap" rel="stylesheet">
<style>
:root{
  --page:#ffffff;
  --band:#d9a25a;
  --band-dark:#c78c43;
  --banner:#d6a560;
  --banner-line:#f4e2c0;
  --navy:#173a74;
  --brand:#1f4c9c;
  --stripe:#9fb0d2;
  --ink:#4a3524;
  --cream:#fff8ea;
  --table:#e6b874;
  --table-head:#c98f45;
  --rule:#a9773a;
}
*{box-sizing:border-box;margin:0;padding:0}
html,body{width:849px;height:1200px;overflow:hidden;background:var(--page)}
body{position:relative;font-family:"Open Sans",Arial,sans-serif;color:var(--ink)}
.board{position:absolute;left:0;top:0}
.ribbon{position:absolute;left:26px;top:0;width:32px;height:715px;
  background:repeating-linear-gradient(90deg,var(--stripe) 0 2px,#fff 2px 5px);
  clip-path:polygon(0 0,100% 0,100% 100%,50% 96%,0 100%)}
.title-banner{position:absolute;left:160px;top:0;width:530px;height:122px;background:var(--banner);
  box-shadow:0 2px 4px rgba(0,0,0,.25);text-align:center;color:var(--cream)}
.title-banner::after{content:"";position:absolute;inset:6px;border:1px solid var(--banner-line)}
.title{font-size:44px;font-weight:400;margin-top:16px;line-height:1;display:inline-block;
  border-bottom:1.5px solid var(--cream);padding:0 6px 8px 56px;position:relative}
.title .hat{position:absolute;left:4px;top:0;width:44px;height:40px;border-radius:50% 50% 6px 6px;background:var(--cream);opacity:.85}
.subtitle{font-size:24px;margin-top:10px}
.step{position:absolute;left:10px;width:812px;height:130px;
  background:linear-gradient(180deg,var(--band) 0%,var(--band-dark) 100%);
  clip-path:polygon(0 0,100% 0,97% 50%,100% 100%,0 100%);
  box-shadow:0 2px 3px rgba(0,0,0,.2)}
.step-num{position:absolute;left:29px;top:43px;width:44px;height:44px;border-radius:50%;background:var(--navy);
  border:2px solid var(--cream);color:#fff;font-size:32px;text-align:center;line-height:40px}
.photo{position:absolute;top:10px;width:150px;height:110px;border:3px solid #fff;
  background:linear-gradient(135deg,#9a9b98,#d8d2c2 55%,#b9b3a4)}
.photo.a{left:88px}.photo.b{left:260px}
.step ul{position:absolute;left:428px;top:8px;width:340px;list-style:none;font-size:14px;line-height:19px;color:var(--ink)}
.step li{text-indent:-8px;padding-left:8px;margin-bottom:7px}
.step li::before{content:"•"}
.step.tight ul{top:6px}
.step.tight li{margin-bottom:1px}
.recipe{position:absolute;left:66px;top:942px;width:718px;height:180px;background:var(--table);border-radius:8px}
.recipe-ribbon{position:absolute;top:950px;height:48px;width:70px;background:var(--table-head)}
.recipe-ribbon.l{left:14px;clip-path:polygon(0 0,100% 0,100% 100%,0 100%,22% 50%)}
.recipe-ribbon.r{left:765px;clip-path:polygon(0 0,100% 0,78% 50%,100% 100%,0 100%)}
.recipe table{position:absolute;left:0;top:8px;width:718px;border-collapse:collapse;font-size:15px}
.recipe th{background:var(--table-head);color:var(--cream);font-weight:400;height:48px;line-height:1.1;border-left:1px solid var(--rule)}
.recipe th:first-child{text-align:left;padding-left:8px;border-left:none}
.recipe td{height:40px;border-left:1px solid var(--rule);border-bottom:1px solid var(--rule);text-align:center;color:var(--ink)}
.recipe td:first-child{text-align:left;padding-left:8px;border-left:none}
.recipe tr:last-child td{border-bottom:none}
.recipe td.v{text-align:left;padding-left:18px}
.brand{position:absolute;left:0;width:849px;top:1136px;text-align:center}
.brand-name{font-size:50px;font-weight:600;color:var(--brand);line-height:1}
</style>
</head>
<body>
<svg class="board" width="849" height="1200" aria-hidden="true">
  <defs>
    <linearGradient id="boardFill" x1="0" y1="0" x2="0" y2="1">
      <stop offset="0" stop-color="#eaa661"/><stop offset="1" stop-color="#e39750"/>
    </linearGradient>
  </defs>
  <path d="M20 0 H800 A30 30 0 0 0 830 30 V865 A22 22 0 0 0 808 887 H42 A22 22 0 0 0 20 865 Z" fill="url(#boardFill)"/>
</svg>

<div class="ribbon"></div>

<header class="title-banner">
  <h1 class="title"><span class="hat" role="img" aria-label="Chef hat icon"></span>Scone Perfection</h1>
  <p class="subtitle">Best Practice for perfect scone making</p>
</header>

<section class="step" style="top:148px">
  <div class="step-num">1</div>
  <div class="photo a" role="img" aria-label="Scone mix in mixing bowl beside water jug"></div>
  <div class="photo b" role="img" aria-label="Dough hook mixing scone ingredients"></div>
  <ul>
    <li>Weigh ingredients into bowl and weigh off cold water into jug</li>
    <li>Add together into bowl</li>
    <li>Mix the ingredients thoroughly on slow speed for 30 seconds using a dough hook</li>
  </ul>
</section>

<section class="step tight" style="top:292px">
  <div class="step-num">2</div>
  <div class="photo a" role="img" aria-label="Mixed dough beside bowl of grated cheese"></div>
  <div class="photo b" role="img" aria-label="Flavoured scone dough on bench"></div>
  <ul>
    <li>Scrape sides of bowl</li>
    <li>Mix for 15 seconds on second speed Weigh off flavours</li>
    <li>Add to mixed dough, and on slow speed mix thoroughly thru</li>
    <li>Do not over mix</li>
  </ul>
</section>

<section class="step" style="top:436px">
  <div class="step-num">3</div>
  <div class="photo a" role="img" aria-label="Rounded scone dough on floured bench"></div>
  <div class="photo b" role="img" aria-label="Smooth dough round with cutter"></div>
  <ul>
    <li>Tip onto floured bench and gently round up till a smooth surface</li>
    <li>Do not knead or beat</li>
    <li>Rest for 10 minutes</li>
  </ul>
</section>

<section class="step" style="top:582px">
  <div class="step-num">4</div>
  <div class="photo a" role="img" aria-label="Rolling pin over dough round"></div>
  <div class="photo b" role="img" aria-label="Dough rolled out flat with cutter"></div>
  <ul>
    <li>Pin / roll out dough gently till you reach your plate size or about 1cm thickness</li>
    <li>Pin / roll out round if using a round cutter to cut down on rework scone dough</li>
  </ul>
</section>

<section class="step" style="top:725px">
  <div class="step-num">5</div>
  <div class="photo a" role="img" aria-label="Reworked dough scraps with cutter"></div>
  <div class="photo b" role="img" aria-label="Tray of cut scones ready to bake"></div>
  <ul>
    <li>Rework equals tougher scones</li>
    <li>Rework scrape gently, rest before cutting avoid doing this step more than once if possible</li>
    <li>Tray up evenly, rest for 5 minutes</li>
    <li>Bake at 210°C -220°C for 15-20minutes</li>
  </ul>
</section>

<div class="recipe-ribbon l"></div>
<div class="recipe-ribbon r"></div>
<section class="recipe">
  <table>
    <colgroup><col style="width:155px"><col style="width:48px"><col style="width:92px"><col style="width:120px"><col style="width:92px"><col style="width:71px"><col style="width:140px"></colgroup>
    <thead>
      <tr><th>Scone Recipe</th><th></th><th>Cheese</th><th>Cheese &amp;<br>Onion</th><th>Sultana</th><th>Date</th><th>Spinach &amp; Feta</th></tr>
    </thead>
    <tbody>
      <tr><td>PRIMA SCONE MIX</td><td></td><td class="v">1.600</td><td></td><td></td><td></td><td></td></tr>
      <tr><td>Water</td><td></td><td class="v">0.900</td><td></td><td></td><td></td><td></td></tr>
      <tr><td>Total</td><td>2.500</td><td>0.300</td><td>0.200 &amp; 0.100</td><td>0.300</td><td>0.300</td><td>0.200 &amp; 0.100</td></tr>
    </tbody>
  </table>
</section>

<footer class="brand">
  <span class="brand-name">Florwick</span>
</footer>
</body>
</html>
```